Web Design for Independent Pet Supply shop.

Larchmont Critter Depot is a locally owned and operated premium natural pet food store and supply company with 2 thriving retail stores in Bend, Oregon, and a home delivery service. The pet food offered is the best on the market and may be described as “holistic”. Also on offer is a vast selection of toys, training tools, treats, and other supplies, as well as dog washing services that range from "do-it yourself" to "spa." Current site: LarchmontCritterDepot.com. They need a new, updated and responsive site.
Likes:
Vondals.com: Natural colors, not loud, pages in motion, simple & clean but very informative.
Tobiasmerrow.com: Everything in simple big colorful blocks. The specials run across the top and in motion. This site looks very professional but simple. The information is available several different places.
Greenbarrel.com: Again big blocks through out. Very Fun and inviting. Tons of information with videos and recipes and testimonials. Pleasant feel and colors as well.
Dislikes:
Furvana.com: Looks cheap, hate the colors, very busy and over whelming. Hate the old style header bar going across with options. Too many printed words instead of fun images.
Colors should be "natural" tones, warm and soothing. Deep dark blue and greys with earthy wood color.
Do Not Use: Blue violet, violet, red violet

```html
<!DOCTYPE html>
<html lang="en">
<head>
<meta charset="utf-8">
<title>Larchmont Critter Depot</title>
<link rel="stylesheet" href="https://fonts.googleapis.com/css2?family=Lato:wght@400;700&family=Montserrat:wght@700&display=swap">
<style>
  :root {
    --header-bg: #ffffff;
    --brand-brown: #b27a3a;
    --nav-text: #3a3a3a;
    --hero-text: #ffffff;
    --btn-product: #e8655a;
    --btn-resource: #1f9e6c;
    --grass-light: #8fae3c;
    --grass-mid: #6b8c2a;
    --grass-dark: #3f5a18;
    --fur-gold: #dba05a;
    --fur-deep: #b9793a;
    --sun-glow: #e8d27a;
    --shadow-bg: #1e1a10;
  }
  * { margin: 0; padding: 0; box-sizing: border-box; }
  html, body { width: 1200px; height: 556px; overflow: hidden; }
  body { font-family: "Lato", sans-serif; background: var(--header-bg); }

  .page { position: relative; width: 1200px; height: 556px; overflow: hidden; }

  .site-header {
    position: absolute; top: 0; left: 0; right: 0; height: 62px;
    background: var(--header-bg);
    display: flex; align-items: center; justify-content: space-between;
    padding: 0 119px 0 123px;
    z-index: 2;
  }
  .brand {
    display: flex; align-items: center; gap: 7px;
    font-weight: 700; font-size: 15px; letter-spacing: 0.2px;
    text-transform: uppercase; color: var(--brand-brown); text-decoration: none;
  }
  .brand-dot { width: 22px; height: 22px; border-radius: 50%; background: var(--brand-brown); }
  .main-nav { display: flex; gap: 17px; }
  .main-nav a {
    font-size: 13px; color: var(--nav-text); text-decoration: none;
    text-transform: uppercase; letter-spacing: 0.1px;
  }

  .hero { position: absolute; top: 62px; left: 0; right: 0; bottom: 0; }
  .hero-photo {
    position: absolute; inset: 0;
    background:
      radial-gradient(ellipse 230px 330px at 690px 250px, rgba(219,160,90,0.95), rgba(185,121,58,0.6) 55%, rgba(185,121,58,0) 80%),
      radial-gradient(ellipse 200px 140px at 420px 60px, rgba(232,210,122,0.75), rgba(232,210,122,0) 75%),
      radial-gradient(ellipse 300px 150px at 130px 40px, rgba(170,180,70,0.8), rgba(170,180,70,0) 75%),
      radial-gradient(ellipse 420px 260px at 1120px 60px, rgba(30,26,16,0.95), rgba(30,26,16,0) 80%),
      linear-gradient(180deg, #5e6a2a 0%, var(--grass-light) 42%, var(--grass-mid) 70%, var(--grass-dark) 100%);
  }
  .hero-shade { position: absolute; inset: 0; background: rgba(20,14,6,0.18); }

  .hero-content { position: absolute; left: 0; right: 0; top: 181px; text-align: center; }
  .hero-title {
    font-family: "Montserrat", sans-serif; font-weight: 700;
    font-size: 43px; letter-spacing: 0.8px; color: var(--hero-text); line-height: 1.1;
  }
  .hero-actions { display: flex; justify-content: center; gap: 17px; margin-top: 49px; }
  .btn {
    display: inline-flex; align-items: center; justify-content: center;
    height: 39px; border-radius: 3px;
    font-weight: 700; font-size: 11.5px;
    color: var(--hero-text); text-decoration: none; text-transform: uppercase;
  }
  .btn-product { width: 117px; background: var(--btn-product); }
  .btn-resource { width: 121px; background: var(--btn-resource); }
</style>
</head>
<body>
<div class="page">
  <header class="site-header">
    <a class="brand" href="#"><span class="brand-dot"></span>Larchmont Critter Depot</a>
    <nav class="main-nav">
      <a href="#">About</a>
      <a href="#">Blog</a>
      <a href="#">Contact</a>
      <a href="#">Dog Wash</a>
      <a href="#">Event</a>
      <a href="#">Home</a>
      <a href="#">Product</a>
      <a href="#">Resources</a>
    </nav>
  </header>

  <section class="hero">
    <div class="hero-photo" role="img" aria-label="Photo of a golden retriever lying in sunlit green grass in a garden"></div>
    <div class="hero-shade"></div>
    <div class="hero-content">
      <h1 class="hero-title">WE CARE FOR EVERY PET</h1>
      <div class="hero-actions">
        <a class="btn btn-product" href="#">Product</a>
        <a class="btn btn-resource" href="#">Resource</a>
      </div>
    </div>
  </section>
</div>
</body>
</html>
```